Webdesign für eine Metallfirma
Zielgruppe
Der Auftraggegeber ist eine Metallfirma, welche sich mit Metallbau, Parktechnik,Preßwerkzeugen,Stadtmöblierung
und neu mit Erneuerbaren Energien beschäftigt.
Zielgruppe sind sowohl private als auch geschäftliche Partner, aber auch Städte und Gemeinden.
Aufgabenstellung
- das Layout benötigen wir als PSD
- nur die Startseite soll gelayoutet werden
- die vorherrschende Farbe orientiert sich am Logo, gewünscht ist eine weitere Farbe, da verlassen wir uns auf Ihren Geschmack (siehe anbei)
- die Inhalte der beiden angegebenen Webseiten sollen zusammengeführt werden (siehe unten)
- bitte lassen Sie die Navigationspunkte in allen Ebenen aufklappen

```html
<!DOCTYPE html>
<html lang="de">
<head>
<meta charset="utf-8">
<title>Kolbrand – Startseite</title>
<link href="https://fonts.googleapis.com/css2?family=PT+Sans:ital,wght@0,400;0,700;1,400&family=Poppins:wght@300;400;500&display=swap" rel="stylesheet">
<style>
:root{
  --blue:#3d8bd4;
  --blue-dark:#2f78c0;
  --text:#4a4a4a;
  --muted:#777;
  --light:#fafafa;
  --line:#eef3f8;
}
*{margin:0;padding:0;box-sizing:border-box}
html,body{width:1200px;height:1200px;overflow:hidden;background:#fff}
body{position:relative;font-family:"Poppins",sans-serif;color:var(--text)}
.page{position:absolute;left:387px;top:22px;width:692px;height:1865px;background:#fff;transform:scale(0.625);transform-origin:0 0;box-shadow:0 0 8px rgba(0,0,0,.18);overflow:hidden}
.abs{position:absolute}
.heading{font-family:"PT Sans",sans-serif}
.topbar{right:10px;top:6px;font-family:"PT Sans",sans-serif;font-style:italic;font-size:8.5px;color:var(--blue)}
.brand{left:20px;top:32px;display:flex;align-items:center;gap:8px}
.brand-square{width:26px;height:26px;background:var(--blue)}
.brand-name{font-family:"PT Sans",sans-serif;font-weight:700;font-size:11px;line-height:13px;color:var(--blue)}
.mainnav{right:10px;top:49px;display:flex;gap:11px;font-family:"Poppins",sans-serif;font-weight:500;font-size:7px;color:#333}
.mainnav .active{color:var(--blue)}
.hero{left:0;top:71px;width:692px;height:289px;background:linear-gradient(120deg,#c9b9a0 0%,#9c9486 35%,#8a98a8 65%,#c8c4be 100%)}
.tabs{left:0;top:360px;width:692px;height:57px;border-bottom:3px solid var(--line);display:flex;align-items:center;padding-left:12px;font-family:"PT Sans",sans-serif;font-size:11.5px;color:#444}
.tabs span{margin-right:43px}
.intro{left:0;top:466px;width:692px;text-align:center}
.intro h1{font-family:"PT Sans",sans-serif;font-weight:400;font-size:14px;color:#444;margin-bottom:8px}
.intro p{font-size:11.5px;line-height:14.5px;font-weight:300;color:#555}
.about-panel{left:330px;top:585px;width:352px;height:224px;background:var(--light)}
.about-photo{left:20px;top:585px;width:310px;height:224px;background:linear-gradient(180deg,#d9dfe4 0%,#9aa3aa 45%,#3f4650 100%)}
.about-text{left:353px;top:585px;width:300px}
.about-text h2{font-family:"PT Sans",sans-serif;font-weight:400;font-size:12px;color:#444;margin-bottom:14px}
.about-text p{font-size:8px;line-height:12.2px;font-weight:300;color:#555}
.btn{left:353px;top:751px;width:131px;height:28px;background:var(--blue);color:#fff;font-size:7.5px;display:flex;align-items:center;justify-content:center}
.feature{top:860px;display:flex;gap:8px;align-items:center}
.feature h3{font-family:"PT Sans",sans-serif;font-weight:400;font-size:12.5px;color:#444}
.feature p{font-size:7.5px;line-height:12px;font-weight:300;color:#666}
.services-head{left:0;top:955px;width:692px;text-align:center}
.services-head h2{font-family:"PT Sans",sans-serif;font-weight:400;font-size:12px;color:#444;margin-bottom:20px}
.services-head p{font-size:7.8px;line-height:12.5px;font-weight:300;color:#666}
.tile-label{font-family:"PT Sans",sans-serif;font-weight:700;font-size:12px;color:#444}
.tile{width:220px;height:144px}
.t-metal{background:linear-gradient(135deg,#e4e6e8,#8d9296 60%,#3a3d40)}
.t-park{background:linear-gradient(135deg,#1f56a8,#2d6fcc 60%,#d4b49a)}
.t-press{background:linear-gradient(135deg,#6b6660,#c9c5c0 50%,#ece9e6)}
.t-solar{background:linear-gradient(180deg,#7fb0e0 0%,#cfe2f4 40%,#33497e 65%,#6c8f3c 100%)}
.t-bench{background:linear-gradient(180deg,#4f6e2e 0%,#86a64a 55%,#5d8a30 100%)}
.cta{left:0;top:1438px;width:692px;height:114px;background:var(--blue);color:#fff}
.cta h2{position:absolute;left:40px;top:34px;font-family:"PT Sans",sans-serif;font-weight:700;font-size:12.5px}
.cta p{position:absolute;left:40px;top:58px;width:430px;font-size:7.8px;line-height:11px;font-weight:300}
.cta-btn{position:absolute;left:507px;top:61px;width:160px;height:29px;border:1px solid #fff;display:flex;align-items:center;justify-content:center;font-family:"PT Sans",sans-serif;font-weight:700;font-size:11.5px}
.contacts-head{left:0;top:1593px;width:692px;text-align:center;font-family:"PT Sans",sans-serif;font-weight:700;font-size:12px;line-height:17px;color:#444}
.contact-col{top:1668px;font-size:6.6px;line-height:11px;color:#555}
.contact-col h4{font-weight:400;font-size:6.6px;margin-bottom:10px;color:#555}
.contact-col .name{margin-bottom:10px}
.divider{left:0;top:1787px;width:692px;height:2px;background:var(--line)}
.footer{top:1811px;font-size:6px;color:#555}
.footer-links{top:1846px;left:20px;display:flex;gap:20px;font-size:5.6px;color:#555}
</style>
</head>
<body>
<div class="page">
  <div class="abs topbar">Tel.: +49 (0) 12345 670-0 &nbsp;&nbsp;I&nbsp;&nbsp; E-Mail: info@kolbrand-metall.de</div>
  <div class="abs brand">
    <div class="brand-square"></div>
    <div class="brand-name">Kolbrand Metall- und<br>Anlagenbau GmbH</div>
  </div>
  <nav class="abs mainnav">
    <span class="active">HOME</span><span>WER WIR SIND</span><span>PRODUKTE</span><span>KARRIERE</span><span>AKTUELLES</span><span>KONTAKT</span>
  </nav>
  <div class="abs hero" role="img" aria-label="Foto: zwei lächelnde Mitarbeiter in einer Werkhalle, einer mit gelbem Schutzhelm, einer mit Tablet"></div>
  <div class="abs tabs"><span>METALLBAU</span><span>PARKTECHNIK</span><span>PRESSWERKZEUGE</span><span>STADTMÖBLIERUNG</span><span>ERNEUERBARE ENERGIEN</span></div>

  <section class="abs intro">
    <h1>Kolbrand - Ihr verlässlicher Partner</h1>
    <p>Wir sind im Metallbau,&nbsp; Parktechnik, Presswerkzeuge,<br>Stadtmöblierung und erneuerbare Energien tätig.<br>Lorem ipsum dolor sit amet, consectetuer adipising elit.</p>
  </section>

  <div class="abs about-panel"></div>
  <div class="abs about-photo" role="img" aria-label="Foto: Team aus fünf Mitarbeitenden in einem hellen Büro"></div>
  <div class="abs about-text">
    <h2>WER WIR SIND</h2>
    <p>Lorem ipsum dolor sit amet, consectetuer adipiscing elit. Aenean commodo ligula eget dolor. Aenean massa. Cum sociis natoque penatibus et magnis dis parturient montes, nascetur ridiculus mus. Donec quam felis, ultricies nec, pellentesque eu, pretium quis, sem. Nulla consequat massa quis enim. Donec pede justo, fringilla vel, aliquet nec, vulputate eget, arcu. In enim justo, rhoncus ut, imperdiet a, venenatis vitae, justo. Nullam dictum felis eu pede mollis pretium. Integer tincidunt. Cras dapibus.</p>
  </div>
  <div class="abs btn">Mehr zum Unternehmen</div>

  <div class="abs feature" style="left:43px">
    <svg width="28" height="24" viewBox="0 0 28 24"><path d="M2 13 L10 21 L26 3" fill="none" stroke="#3d8bd4" stroke-width="4"/></svg>
    <div><h3>Lorem Ipsum dolor</h3><p>Donec quam felis, ultricies nec,<br>pellentesque eu, pretium quis,</p></div>
  </div>
  <div class="abs feature" style="left:256px">
    <svg width="28" height="24" viewBox="0 0 28 24"><path d="M2 13 L10 21 L26 3" fill="none" stroke="#3d8bd4" stroke-width="4"/></svg>
    <div><h3>Lorem Ipsum dolor</h3><p>Donec quam felis, ultricies nec,<br>pellentesque eu, pretium quis,</p></div>
  </div>
  <div class="abs feature" style="left:465px">
    <svg width="28" height="24" viewBox="0 0 28 24"><path d="M2 13 L10 21 L26 3" fill="none" stroke="#3d8bd4" stroke-width="4"/></svg>
    <div><h3>Lorem Ipsum dolor</h3><p>Donec quam felis, ultricies nec,<br>pellentesque eu, pretium quis,</p></div>
  </div>

  <section class="abs services-head">
    <h2>WAS WIR TUN</h2>
    <p>Donec quam felis, ultricies nec, pellentesque eu, pretium quis, sem.<br>Nulla consequat massa quis enim. Donec pede justo, fringilla vel,<br>aliquet nec, vulputate eget, arcu.</p>
  </section>

  <div class="abs tile-label" style="left:9px;top:1059px">Metallbau</div>
  <div class="abs tile t-metal" style="left:9px;top:1077px" role="img" aria-label="Foto: gestapelte Metallprofile und Rohre"></div>
  <div class="abs tile-label" style="left:238px;top:1059px">Parktechnik</div>
  <div class="abs tile t-park" style="left:236px;top:1077px" role="img" aria-label="Foto: Hand zieht ein Parkticket aus einem blauen Automaten"></div>
  <div class="abs tile-label" style="left:463px;top:1059px">Presswerkzeuge</div>
  <div class="abs tile t-press" style="left:463px;top:1077px" role="img" aria-label="Foto: Handwerker verpresst Rohre mit einem Presswerkzeug"></div>
  <div class="abs tile-label" style="left:122px;top:1241px">Stadtmöblierung</div>
  <div class="abs tile t-solar" style="left:122px;top:1259px" role="img" aria-label="Foto: Solarfeld mit Windrädern unter blauem Himmel"></div>
  <div class="abs tile-label" style="left:349px;top:1241px">Erneuerbare Energien</div>
  <div class="abs tile t-bench" style="left:349px;top:1260px" role="img" aria-label="Foto: Parkbank auf einer Wiese vor grünen Bäumen"></div>

  <section class="abs cta">
    <h2>Sie haben Fragen? Wir beraten Sie gerne. Nehmen Sie Kontakt mit uns auf.</h2>
    <p>Lorem ipsum dolor sit amet, consectetuer adipiscing elit. Aenean commodo ligula eget dolor. Aenean massa. Cum sociis natoque penatibus et magnis dis parturient montes, nascetur ridiculus mus. Donec quam felis,</p>
    <div class="cta-btn">E-Mail schreiben</div>
  </section>

  <div class="abs contacts-head">Unsere Ansprechpartner in den Fachbereichen stehen Ihnen gerne telefonisch<br>oder per E-Mail zur Verfügung</div>

  <div class="abs contact-col" style="left:62px"><h4>PARKTECHNIK</h4><div class="name">Herr Lindner</div>Telefon: +49 (0) 12345 670-114<br>E-Mail: m.lindner@kolbrand-metall.de</div>
  <div class="abs contact-col" style="left:200px"><h4>METALLBAU</h4><div class="name">Herr Brandt</div>Telefon: +49 (0) 12345 670-113<br>E-Mail: j.brandt@kolbrand-metall.de</div>
  <div class="abs contact-col" style="left:340px"><h4>SANITÄRTECHNIK &amp; ERNEUERBARE EENERGIEN</h4><div class="name">Herr Vogt</div>Telefon: +49 (0) 12345 670-108<br>E-Mail: s.vogt@kolbrand-metall.de</div>
  <div class="abs contact-col" style="left:520px"><h4>GESCHÄFTSLEITUNG</h4>Telefon: +49 (0) 12345 670-0<br>Telefax: +49 (0) 12345 670-130<br>E-Mail:&nbsp; info@kolbrand-metall.de</div>

  <div class="abs divider"></div>
  <div class="abs footer" style="left:19px">Kolbrand Metall- und Anlagenbau GmbH</div>
  <div class="abs footer" style="left:207px">Werkstraße 12 &nbsp;I&nbsp; 09100 Musterstadt, Erzgebirge</div>
  <div class="abs footer" style="left:365px">Tel.: +49 (0) 12345 670-0 &nbsp;I&nbsp; Fax: +49 (0) 12345 670-130</div>
  <div class="abs footer" style="left:566px">E-Mail: info@kolbrand-metall.de</div>
  <div class="abs footer-links"><span>Datenschutz</span><span>Impressum</span><span style="margin-left:14px">Copyright Kolbrand 2022</span></div>
</div>
</body>
</html>
```